VORLEN Website Design

We need a website designed for our company VORLEN. We are a luxury lifestyle club that will provide benefits and services for our members. The site should be clean & sleek, preferably using black and white (or darker colors). (example sites: brimvale.example, tusko.example)

Here is a link of a sample page I did using wix. (https://pelmundry4.sitebuild.example/mypage) This can be used to get a general idea.

Target Market(s)

Upper Middle Class in the United States

Number of Pages Required

5+ page

Font styles to use
Sans Serif
Other font styles liked:
• Arial (or other similar fonts)

Requirements
Must have
• A clean design that is eye-catching and speaks to our company.
Nice to have
• Ideas for copy.

```html
<!DOCTYPE html>
<html lang="en">
<head>
<meta charset="utf-8">
<title>VORLEN — A Members Only Lifestyle Club</title>
<link rel="stylesheet" href="https://fonts.googleapis.com/css2?family=Montserrat:ital,wght@0,300;0,400;0,500;0,600;0,700;1,400&display=swap">
<style>
  :root {
    --black: #000000;
    --ink: #0a0a0a;
    --band: #121212;
    --white: #ffffff;
    --soft: #d8d8d8;
    --muted: #9a9a9a;
    --line: #bdbdbd;
  }
  * { box-sizing: border-box; margin: 0; padding: 0; }
  html, body { width: 1200px; height: 3922px; overflow: hidden; }
  body { background: var(--black); color: var(--white); font-family: "Montserrat", Arial, sans-serif; position: relative; }

  .site-header { position: absolute; top: 0; left: 0; width: 1200px; height: 110px; background: var(--black); }
  .brand { position: absolute; left: 26px; top: 32px; font-size: 40px; font-weight: 300; letter-spacing: 1px; }
  .main-nav { position: absolute; left: 371px; top: 46px; display: flex; gap: 44px; font-size: 14px; font-weight: 600; text-transform: uppercase; letter-spacing: .5px; }
  .account-links { position: absolute; left: 1001px; top: 37px; display: flex; gap: 18px; }
  .account-links a { display: block; width: 72px; height: 36px; line-height: 34px; text-align: center; border: 1.5px solid var(--line); font-size: 13px; font-weight: 600; color: var(--white); text-decoration: none; }

  .btn { display: inline-block; border: 1.5px solid var(--line); color: var(--white); text-decoration: none; text-align: center; font-size: 15px; letter-spacing: .5px; }

  .hero { position: absolute; top: 110px; left: 0; width: 1200px; height: 706px; background: radial-gradient(ellipse at 50% 30%, #8a6a3a 0%, #4a3518 40%, #1a1208 80%, #0c0804 100%); }
  .hero-title { position: absolute; top: 240px; width: 100%; text-align: center; font-size: 50px; font-weight: 300; line-height: 68px; letter-spacing: 3px; text-transform: uppercase; }
  .hero-actions { position: absolute; top: 434px; left: 429px; display: flex; gap: 21px; }
  .hero-actions .btn { width: 162px; height: 44px; line-height: 41px; text-transform: uppercase; font-size: 14px; }

  .feature { position: absolute; left: 0; width: 1200px; background: var(--black); }
  .feature-media { position: absolute; top: 0; width: 609px; height: 100%; }
  .feature-body { position: absolute; top: 0; }
  .feature-title { font-size: 40px; font-weight: 300; letter-spacing: 2px; text-transform: uppercase; white-space: nowrap; margin-bottom: 36px; }
  .feature-text { font-size: 16px; line-height: 36px; color: var(--soft); white-space: nowrap; }
  .feature .btn { margin-top: 38px; width: 144px; height: 40px; line-height: 37px; font-size: 14px; }

  .about { top: 816px; height: 509px; }
  .about .feature-media { left: 0; background: linear-gradient(135deg, #1a2a8a 0%, #3a60d0 35%, #8a5a20 65%, #0a0a30 100%); }
  .about .feature-body { left: 648px; top: 70px; width: 530px; }
  .benefits { top: 1325px; height: 510px; }
  .benefits .feature-media { left: 611px; width: 589px; background: linear-gradient(180deg, #6a9ad8 0%, #b8d0ea 45%, #e8e8e8 60%, #7a7a7a 100%); }
  .benefits .feature-body { left: 44px; top: 56px; width: 540px; }
  .experiences { top: 1835px; height: 505px; }
  .experiences .feature-media { left: 0; background: radial-gradient(ellipse at 60% 35%, #fff3dd 0%, #c8906a 25%, #6a3a30 60%, #1a0c0c 100%); }
  .experiences .feature-body { left: 644px; top: 64px; width: 530px; }

  .showcase { position: absolute; top: 2340px; left: 0; width: 1200px; height: 496px; background: radial-gradient(ellipse at 50% 50%, #5a2a4a 0%, #2a1420 55%, #120a10 100%); }
  .showcase-title { position: absolute; left: 144px; top: 192px; font-size: 50px; line-height: 56px; text-transform: uppercase; letter-spacing: -.5px; }
  .showcase-title .strong { font-weight: 700; }
  .showcase-title .light { font-weight: 300; }
  .showcase-title .indent { padding-left: 130px; }
  .video { position: absolute; left: 648px; top: 117px; width: 445px; height: 275px; background: linear-gradient(135deg, #3a1a5a 0%, #b03a7a 40%, #2a2060 75%, #120c20 100%); box-shadow: 0 6px 20px rgba(0,0,0,.6); }
  .video svg { position: absolute; left: 185px; top: 104px; }

  .testimonial { position: absolute; top: 2836px; left: 0; width: 1200px; height: 384px; background: var(--band); }
  .quote-mark { position: absolute; top: 60px; width: 100%; text-align: center; font-size: 70px; font-weight: 700; color: #3a3a3a; line-height: 1; }
  .avatar { position: absolute; left: 136px; top: 131px; width: 126px; height: 126px; border-radius: 50%; background: linear-gradient(180deg, #c8b8a0 0%, #6a6a78 100%); border: 3px solid #e8d8b8; }
  .quote-text { position: absolute; left: 298px; top: 128px; width: 800px; font-size: 21px; line-height: 34px; color: var(--muted); font-weight: 400; white-space: nowrap; }
  .quote-author { position: absolute; left: 304px; top: 256px; font-size: 14px; font-style: italic; color: #6a6a6a; }
  .slider-arrow { position: absolute; top: 181px; width: 46px; height: 46px; background: #2a2a2a; display: flex; align-items: center; justify-content: center; }
  .slider-arrow.prev { left: 0; }
  .slider-arrow.next { right: 0; }

  .join { position: absolute; top: 3220px; left: 0; width: 1200px; height: 335px; background: var(--black); text-align: center; }
  .join-tagline { position: absolute; top: 70px; width: 100%; font-size: 36px; font-weight: 300; color: var(--soft); text-transform: uppercase; }
  .join-title { position: absolute; top: 128px; width: 100%; font-size: 42px; font-weight: 400; text-transform: uppercase; letter-spacing: 2px; }
  .join .btn { position: absolute; left: 529px; top: 224px; width: 152px; height: 44px; line-height: 41px; font-size: 15px; text-transform: uppercase; }

  .site-footer { position: absolute; top: 3555px; left: 0; width: 1200px; height: 367px; background: var(--black); }
  .footer-brand { position: absolute; left: 100px; top: 56px; font-size: 42px; font-weight: 300; letter-spacing: 1px; }
  .footer-links { position: absolute; left: 100px; top: 134px; display: grid; grid-template-columns: auto auto auto; column-gap: 26px; row-gap: 14px; font-size: 17px; font-weight: 500; }
  .social { position: absolute; left: 775px; top: 94px; display: flex; gap: 32px; }
  .social span { width: 46px; height: 46px; border-radius: 50%; background: var(--white); display: block; }
  .copyright { position: absolute; right: 94px; top: 254px; font-size: 15px; color: var(--soft); }
</style>
</head>
<body>

<header class="site-header">
  <div class="brand">VORLEN</div>
  <nav class="main-nav"><span>Home</span><span>About</span><span>Services &amp; Benefits</span><span>Contact</span></nav>
  <div class="account-links"><a href="#">JOIN</a><a href="#">LOGIN</a></div>
</header>

<section class="hero" role="img" aria-label="Rows of champagne flutes on a warmly lit bar">
  <h1 class="hero-title">A Members Only<br>Lifestyle Club</h1>
  <div class="hero-actions"><a class="btn" href="#">Join Now</a><a class="btn" href="#">Visit a Club</a></div>
</section>

<section class="feature about">
  <div class="feature-media" role="img" aria-label="Vintage typewriter on a bar counter lit in blue neon"></div>
  <div class="feature-body">
    <h2 class="feature-title">About</h2>
    <p class="feature-text">VORLEN is a members only lifestyle club founded in order<br>to bring the best services, experiences, and opportunities<br>to our diverse community of members.<br>Our members consist of creatives, athletes, artists, and<br>other professionals</p>
    <a class="btn" href="#">Learn More</a>
  </div>
</section>

<section class="feature benefits">
  <div class="feature-body">
    <h2 class="feature-title">Benefits &amp; Services</h2>
    <p class="feature-text">VORLEN Members receive access to the best<br>accountants, attorneys, real estate agents,<br>private bankers/advisers and more.<br>VORLEN members also receive access to private flight<br>travel, premium luxury gym memberships, private<br>social clubs, and private investment opportunities.</p>
    <a class="btn" href="#">Learn More</a>
  </div>
  <div class="feature-media" role="img" aria-label="Travellers stepping off a private jet onto a red carpet"></div>
</section>

<section class="feature experiences">
  <div class="feature-media" role="img" aria-label="Crowd cheering at a concert under bright stage lights"></div>
  <div class="feature-body">
    <h2 class="feature-title">Experiences</h2>
    <p class="feature-text">VORLEN organizes and supports a ton of private events<br>and parties for our members.<br>Members are also provided access to exclusive venues<br>and events from our partners.<br>Network with other members to build lasting<br>relationships.</p>
    <a class="btn" href="#">Learn More</a>
  </div>
</section>

<section class="showcase" role="img" aria-label="Blurred party crowd in the background">
  <div class="showcase-title">
    <div class="strong">Best</div>
    <div class="light">Experience</div>
    <div class="strong indent">Ever</div>
  </div>
  <div class="video" role="img" aria-label="Video still of friends celebrating under confetti">
    <svg width="76" height="58" viewBox="0 0 76 58"><rect width="76" height="58" rx="12" fill="#ffffff" fill-opacity=".85"/><path d="M29 17 L52 29 L29 41 Z" fill="#555"/></svg>
  </div>
</section>

<section class="testimonial">
  <div class="quote-mark">&ldquo;</div>
  <div class="avatar" role="img" aria-label="Portrait of the member quoted"></div>
  <p class="quote-text">&ldquo;Lorem ipsum dolor sit amet, consectetur adipiscing elit. Maecenas<br>bibendum ante quis sagittis pretium. Fusce ac ligula tincidunt,<br>sagittis erat sed, luctus ex. Donec sit amet dignissim libero.</p>
  <p class="quote-author">- Miles Harrow President of the Harrow Group -</p>
  <div class="slider-arrow prev"><svg width="12" height="16" viewBox="0 0 12 16"><path d="M9 2 L3 8 L9 14" stroke="#fff" stroke-width="2" fill="none"/></svg></div>
  <div class="slider-arrow next"><svg width="12" height="16" viewBox="0 0 12 16"><path d="M3 2 L9 8 L3 14" stroke="#fff" stroke-width="2" fill="none"/></svg></div>
</section>

<section class="join">
  <p class="join-tagline">Truly the most exclusive lifestyle club</p>
  <h2 class="join-title">Join Us</h2>
  <a class="btn" href="#">Find a Club</a>
</section>

<footer class="site-footer">
  <div class="footer-brand">VORLEN</div>
  <div class="footer-links">
    <span>Send Feedback</span><span>Gift Cards</span><span>Careers</span>
    <span>Membership</span><span>Press Release</span><span></span>
    <span>Contact Us</span>
  </div>
  <div class="social" aria-label="Social links"><span></span><span></span><span></span><span></span></div>
  <p class="copyright">&copy;2018 VORLEN. All rights reserved.</p>
</footer>

</body>
</html>
```